Business cards — need something that creates “wow” factor

Need a sleek and clean looking business card. Something that is clear and consise. These business cards are for my painting business and hundreds will be placed in the Dallas area between all Halverd Pemberton paint stored. These card really need to stick out! Open to any and all ideas...

Target Market(s)

Residential clientele

Industry/Entity Type

Painting

Contact Information for Business Card

Dorian Vakelby
Owner

382.516.2074

Web: Mesahuepainting.example (still under construction)
Mesahuepainting@mailbox.example

Font styles to use
Sans Serif

Colors

Designer to choose colors to be used in the design.

Requirements
Must have
• My name, number, website, email, Socialpage
• and “100% customer satisfaction guaranteed”
• Socialpage.example/Mesahuepainting/
Nice to have
• Listed services
• Interior/exterior painting
• Drywall repair/texture
• Fence staining/refinishing
• Concrete staining
• Epoxy flooring
• Pressure washing

```html
<!DOCTYPE html>
<html lang="en">
<head>
<meta charset="utf-8">
<title>Mesa Hue — Business Cards</title>
<link href="https://fonts.googleapis.com/css2?family=Montserrat:wght@300;400;500;600&display=swap" rel="stylesheet">
<style>
  :root {
    --page-bg: #1b1b1c;
    --card-light: #f4f4f4;
    --card-dark: #262627;
    --ink-dark: #1e1e1e;
    --ink-muted: #555555;
    --ink-light: #ececec;
    --ink-soft: #bdbdbd;
    --rule-dark: #2a2a2a;
    --accent: #e0442b;
  }
  * { box-sizing: border-box; margin: 0; padding: 0; }
  html, body {
    width: 1200px; height: 900px; overflow: hidden;
    background: var(--page-bg);
    font-family: "Montserrat", sans-serif;
  }
  .canvas {
    width: 1200px; height: 900px;
    display: flex; flex-direction: column; align-items: center; justify-content: center; gap: 40px;
  }
  .card {
    position: relative; width: 640px; height: 365px;
    border-radius: 24px; overflow: hidden;
    box-shadow: 0 18px 40px rgba(0,0,0,.55);
  }
  .card--front { background: var(--card-light); color: var(--ink-dark); }
  .card--back { background: var(--card-dark); color: var(--ink-light); }

  /* brand block */
  .brand { position: absolute; display: flex; flex-direction: column; align-items: center; }
  .brand__row { display: flex; align-items: center; gap: 12px; white-space: nowrap; }
  .brand__dot { width: 16px; height: 16px; border-radius: 50%; background: var(--accent); flex: none; }
  .brand__name { font-size: 36px; font-weight: 600; letter-spacing: 1px; text-transform: uppercase; white-space: nowrap; }
  .brand__tagline { margin-top: 8px; font-size: 9.5px; font-weight: 400; white-space: nowrap; }
  .card--front .brand__tagline { color: var(--ink-muted); }
  .card--back .brand__tagline { color: var(--ink-soft); }

  /* front */
  .card--front .brand { left: 30px; top: 150px; width: 250px; }
  .divider { position: absolute; left: 300px; top: 95px; width: 2px; height: 175px; background: var(--rule-dark); }
  .contact { position: absolute; left: 325px; top: 100px; right: 24px; }
  .contact__name { font-size: 20px; font-weight: 500; letter-spacing: 1px; text-transform: uppercase; white-space: nowrap; }
  .contact__role { font-size: 13px; color: var(--ink-muted); margin-top: 3px; margin-bottom: 16px; }
  .contact__list { list-style: none; }
  .contact__item { display: flex; align-items: center; gap: 10px; font-size: 12px; margin-bottom: 10px; white-space: nowrap; }
  .contact__icon { width: 18px; height: 18px; flex: none; }

  /* back */
  .card--back .brand { left: 45px; top: 95px; width: 270px; }
  .services { position: absolute; left: 360px; top: 70px; list-style: none; }
  .services__item { display: flex; align-items: center; gap: 10px; font-size: 14px; margin-bottom: 10px; white-space: nowrap; }
  .services__tick { width: 15px; height: 15px; flex: none; }
  .guarantee {
    position: absolute; left: 0; right: 0; bottom: 48px;
    display: flex; align-items: center; gap: 10px;
    font-size: 13px; color: var(--ink-light); white-space: nowrap;
  }
  .guarantee__rule { height: 1px; background: var(--ink-soft); }
  .guarantee__rule--left { width: 90px; }
  .guarantee__rule--right { flex: 1; }
  .guarantee__badge { width: 22px; height: 22px; border-radius: 50%; border: 2px solid var(--ink-soft); flex: none; }
</style>
</head>
<body>
<main class="canvas">

  <section class="card card--front" aria-label="Business card front">
    <div class="brand">
      <div class="brand__row"><span class="brand__dot"></span><span class="brand__name">Mesa Hue</span></div>
      <p class="brand__tagline">Commercial | Residential | Interior | Exterior</p>
    </div>
    <div class="divider"></div>
    <div class="contact">
      <h1 class="contact__name">Dorian Vakelby</h1>
      <p class="contact__role">Owner</p>
      <ul class="contact__list">
        <li class="contact__item">
          <svg class="contact__icon" viewBox="0 0 18 18"><circle cx="9" cy="9" r="8" fill="none" stroke="#1e1e1e" stroke-width="1.4"/><path d="M6 5.5l1.6-.3.9 2-1 .8a5 5 0 0 0 2.5 2.5l.8-1 2 .9-.3 1.6c-3.8.3-6.8-2.7-6.5-6.5z" fill="#1e1e1e"/></svg>
          382.516.2074
        </li>
        <li class="contact__item">
          <svg class="contact__icon" viewBox="0 0 18 18"><circle cx="9" cy="9" r="8" fill="none" stroke="#1e1e1e" stroke-width="1.4"/><rect x="5" y="6" width="8" height="6" fill="none" stroke="#1e1e1e" stroke-width="1.2"/><path d="M5 6l4 3.2L13 6" fill="none" stroke="#1e1e1e" stroke-width="1.2"/></svg>
          Mesahuepainting@mailbox.example
        </li>
        <li class="contact__item">
          <svg class="contact__icon" viewBox="0 0 18 18"><circle cx="9" cy="9" r="8" fill="none" stroke="#1e1e1e" stroke-width="1.4"/><path d="M7.5 10.5l3-3M8 6.5l1-1a2 2 0 0 1 3 3l-1 1M10 11.5l-1 1a2 2 0 0 1-3-3l1-1" fill="none" stroke="#1e1e1e" stroke-width="1.2"/></svg>
          Mesahuepainting.example
        </li>
        <li class="contact__item">
          <svg class="contact__icon" viewBox="0 0 18 18"><circle cx="9" cy="9" r="8" fill="none" stroke="#1e1e1e" stroke-width="1.4"/></svg>
          Socialpage.example/Mesahuepainting/
        </li>
      </ul>
    </div>
  </section>

  <section class="card card--back" aria-label="Business card back">
    <div class="brand">
      <div class="brand__row"><span class="brand__dot"></span><span class="brand__name">Mesa Hue</span></div>
      <p class="brand__tagline">Commercial | Residential | Interior | Exterior</p>
    </div>
    <ul class="services">
      <li class="services__item"><svg class="services__tick" viewBox="0 0 16 16"><circle cx="8" cy="8" r="7" fill="none" stroke="#ececec" stroke-width="1.2"/><path d="M5 8.2l2 2 4-4" fill="none" stroke="#ececec" stroke-width="1.3"/></svg>Interior/exterior painting</li>
      <li class="services__item"><svg class="services__tick" viewBox="0 0 16 16"><circle cx="8" cy="8" r="7" fill="none" stroke="#ececec" stroke-width="1.2"/><path d="M5 8.2l2 2 4-4" fill="none" stroke="#ececec" stroke-width="1.3"/></svg>Drywall repair/texture</li>
      <li class="services__item"><svg class="services__tick" viewBox="0 0 16 16"><circle cx="8" cy="8" r="7" fill="none" stroke="#ececec" stroke-width="1.2"/><path d="M5 8.2l2 2 4-4" fill="none" stroke="#ececec" stroke-width="1.3"/></svg>Fence staining/refinishing</li>
      <li class="services__item"><svg class="services__tick" viewBox="0 0 16 16"><circle cx="8" cy="8" r="7" fill="none" stroke="#ececec" stroke-width="1.2"/><path d="M5 8.2l2 2 4-4" fill="none" stroke="#ececec" stroke-width="1.3"/></svg>Concrete staining</li>
      <li class="services__item"><svg class="services__tick" viewBox="0 0 16 16"><circle cx="8" cy="8" r="7" fill="none" stroke="#ececec" stroke-width="1.2"/><path d="M5 8.2l2 2 4-4" fill="none" stroke="#ececec" stroke-width="1.3"/></svg>Epoxy flooring</li>
      <li class="services__item"><svg class="services__tick" viewBox="0 0 16 16"><circle cx="8" cy="8" r="7" fill="none" stroke="#ececec" stroke-width="1.2"/><path d="M5 8.2l2 2 4-4" fill="none" stroke="#ececec" stroke-width="1.3"/></svg>Pressure washing</li>
    </ul>
    <div class="guarantee">
      <span class="guarantee__rule guarantee__rule--left"></span>
      <span class="guarantee__badge"></span>
      <span>100% customer satisfaction guaranteed</span>
      <span class="guarantee__rule guarantee__rule--right"></span>
    </div>
  </section>

</main>
</body>
</html>
```